Business Card Design Project

Doctor, Pain Management. Need a new business card design with appointment info on the back. New address is 18 Birchwood Court, Suite 304, Holloway, NJ 07519. Right now I believe the rest of the information is staying the same.

```html
<!DOCTYPE html>
<html lang="en">
<head>
<meta charset="utf-8">
<title>Gentle Path Pain Care – Business Card</title>
<link rel="stylesheet" href="https://fonts.googleapis.com/css2?family=Montserrat:wght@700;800&family=Tinos:ital,wght@0,400;0,700;1,400&display=swap">
<style>
  :root {
    --bg: #2a2a2c;
    --card-black: #0c0c0d;
    --orange: #e08f2a;
    --gold: #f2c230;
    --gold-deep: #d9a521;
    --blue: #5b8fe0;
    --sky: #7cc4f2;
    --white: #ffffff;
    --ink: #1a1a1a;
    --rule: #333333;
  }
  * { margin: 0; padding: 0; box-sizing: border-box; }
  html, body { width: 1200px; height: 1200px; overflow: hidden; }
  body {
    background: var(--bg);
    font-family: "Tinos", "Times New Roman", serif;
    display: flex;
    flex-direction: column;
    align-items: center;
    justify-content: center;
    gap: 44px;
  }
  .card {
    position: relative;
    width: 920px;
    height: 526px;
    border-radius: 40px;
    overflow: hidden;
    background: var(--card-black);
  }
  .card-bg { position: absolute; inset: 0; }

  /* ---------- appointment side ---------- */
  .contact-list {
    position: absolute; left: 56px; top: 18px;
    list-style: none; color: var(--white);
    font-size: 18px; line-height: 22px;
  }
  .contact-list li { display: flex; align-items: center; gap: 12px; }
  .contact-list svg { width: 16px; height: 16px; fill: var(--white); }
  .brand-mark {
    position: absolute; right: 60px; top: 26px;
    font-family: "Montserrat", sans-serif; font-weight: 800;
    color: var(--sky); letter-spacing: 2px;
  }
  .brand-mark.small { font-size: 96px; line-height: 1; }
  .appt-title {
    position: absolute; left: 420px; top: 122px;
    color: var(--blue); font-size: 28px; letter-spacing: 1px;
  }
  .form-row {
    position: absolute; left: 70px; right: 60px;
    display: flex; align-items: flex-end; gap: 10px;
    color: var(--ink); font-size: 20px;
  }
  .form-row .line { flex: 1; border-bottom: 1.5px solid var(--ink); height: 22px; position: relative; }
  .row-for { top: 170px; }
  .row-days { top: 232px; justify-content: space-between; }
  .day { display: flex; align-items: center; gap: 12px; }
  .tick-box {
    width: 28px; height: 24px; border: 2px solid var(--blue);
    border-radius: 5px; background: #eef3fb;
  }
  .row-when { top: 300px; }
  .row-when .line span { position: absolute; bottom: 0; color: var(--blue); font-size: 16px; }
  .row-when .label-time { margin-left: 26px; }
  .appt-note {
    position: absolute; left: 0; right: 0; top: 466px;
    text-align: center; color: var(--white);
    font-style: italic; font-size: 21px; letter-spacing: 0.5px;
  }
  .appt-note em { color: var(--gold); }

  /* ---------- profile side ---------- */
  .practice-name {
    position: absolute; left: 110px; top: 56px;
    font-family: "Montserrat", sans-serif; font-weight: 800;
  }
  .practice-name .primary { display: block; color: var(--gold); font-size: 62px; line-height: 1; letter-spacing: 1px; }
  .practice-name .secondary { display: block; color: var(--blue); font-size: 34px; line-height: 1.1; letter-spacing: 1px; }
  .practice-tagline {
    position: absolute; left: 110px; top: 160px;
    color: var(--orange); font-style: italic; font-size: 23px;
  }
  .brand-mark.large { top: 108px; right: 70px; font-size: 150px; line-height: 1; }
  .doctor {
    position: absolute; left: 80px; top: 286px;
  }
  .doctor-name { color: var(--gold); font-weight: 700; font-size: 36px; }
  .doctor-title { color: var(--blue); font-style: italic; font-size: 25px; margin-top: 2px; }
  .rule {
    position: absolute; left: 80px; right: 70px; height: 2px; background: var(--orange);
  }
  .rule.top { top: 378px; }
  .online {
    position: absolute; left: 80px; top: 392px; list-style: none;
    color: var(--gold); font-size: 23px; line-height: 30px;
  }
  .online li, .phones li { display: flex; align-items: center; gap: 14px; }
  .online svg { width: 20px; height: 20px; fill: var(--blue); }
  .phones {
    position: absolute; right: 70px; top: 392px; list-style: none;
    color: var(--orange); font-size: 23px; line-height: 30px; text-align: right;
  }
  .phones li { justify-content: flex-end; }
  .phones svg { width: 18px; height: 18px; fill: var(--sky); }
  .rule.bottom { top: 458px; left: 560px; }
  .address {
    position: absolute; right: 70px; top: 466px;
    color: var(--orange); font-size: 22px; line-height: 26px; text-align: right;
  }
</style>
</head>
<body>

<!-- appointment side -->
<section class="card card-appointment" aria-label="Appointment card">
  <svg class="card-bg" viewBox="0 0 920 526" preserveAspectRatio="none" aria-hidden="true">
    <rect width="920" height="526" fill="var(--card-black)"/>
    <path d="M0 0 H470 C560 0 600 80 640 130 C660 150 680 162 700 165 H0 Z" fill="var(--orange)"/>
    <path d="M0 110 H580 C620 112 650 150 700 165 H920 V450 H0 Z" fill="var(--white)"/>
    <path d="M470 0 C560 0 600 80 640 130 C660 150 680 162 700 165" fill="none" stroke="var(--gold)" stroke-width="4"/>
  </svg>

  <ul class="contact-list">
    <li><svg viewBox="0 0 24 24"><path d="M6.6 10.8a15 15 0 0 0 6.6 6.6l2.2-2.2c.3-.3.7-.4 1-.2 1.1.4 2.3.6 3.6.6.6 0 1 .4 1 1V20c0 .6-.4 1-1 1A17 17 0 0 1 3 4c0-.6.4-1 1-1h3.5c.6 0 1 .4 1 1 0 1.3.2 2.5.6 3.6.1.3 0 .7-.2 1z"/></svg>201.555.0148</li>
    <li><svg viewBox="0 0 24 24"><path d="M6 2h12v6H6zM4 9h16a2 2 0 0 1 2 2v6h-4v5H6v-5H2v-6a2 2 0 0 1 2-2zm4 8v3h8v-3z"/></svg>201.555.0163</li>
    <li><svg viewBox="0 0 24 24"><path d="M2 5h20v14H2zm2 2v.5l8 5 8-5V7z"/></svg>gentlepath.office@mailbox.com</li>
    <li><svg viewBox="0 0 24 24"><path d="M12 2a10 10 0 1 0 0 20 10 10 0 0 0 0-20zm0 2c.9 0 2.2 1.7 2.8 5H9.2C9.8 5.7 11.1 4 12 4zM4.3 10h3a19 19 0 0 0 0 4h-3a8 8 0 0 1 0-4zm4.9 0h5.6a17 17 0 0 1 0 4H9.2a17 17 0 0 1 0-4zm7.5 0h3a8 8 0 0 1 0 4h-3a19 19 0 0 0 0-4zM9.2 15h5.6c-.6 3.3-1.9 5-2.8 5s-2.2-1.7-2.8-5z"/></svg>www.gentlepathcare.com</li>
  </ul>

  <div class="brand-mark small">GPC</div>

  <h2 class="appt-title">Appointment</h2>

  <div class="form-row row-for"><span>For :</span><span class="line"></span></div>

  <div class="form-row row-days">
    <span class="day">Mon <span class="tick-box"></span></span>
    <span class="day">Tue <span class="tick-box"></span></span>
    <span class="day">Wed <span class="tick-box"></span></span>
    <span class="day">Thu <span class="tick-box"></span></span>
    <span class="day">Fri <span class="tick-box"></span></span>
    <span class="day">Sat <span class="tick-box"></span></span>
    <span class="day">Sun <span class="tick-box"></span></span>
  </div>

  <div class="form-row row-when">
    <span>Date:</span>
    <span class="line"><span style="left:36%">/</span><span style="left:66%">/</span></span>
    <span class="label-time">Time:</span>
    <span class="line"><span style="left:40%">:</span></span>
  </div>

  <p class="appt-note">If you are <em>unable to keep your appointment</em>, please contact us as soon as possible</p>
</section>

<!-- profile side -->
<section class="card card-profile" aria-label="Business card">
  <h1 class="practice-name">
    <span class="primary">GENTLE PATH</span>
    <span class="secondary">PAIN CARE</span>
  </h1>
  <p class="practice-tagline">Location in New Jersey &amp; New York</p>

  <div class="brand-mark large">GPC</div>

  <div class="doctor">
    <p class="doctor-name">Marian Okafor, M.D., Ph.D.</p>
    <p class="doctor-title">Board Certified Anesthesiologist</p>
  </div>

  <div class="rule top"></div>

  <ul class="online">
    <li><svg viewBox="0 0 24 24"><path d="M2 5h20v14H2zm2 2v.5l8 5 8-5V7z"/></svg>gentlepath.office@mailbox.com</li>
    <li><svg viewBox="0 0 24 24"><path d="M12 2a10 10 0 1 0 0 20 10 10 0 0 0 0-20zm0 2c.9 0 2.2 1.7 2.8 5H9.2C9.8 5.7 11.1 4 12 4zM4.3 10h3a19 19 0 0 0 0 4h-3a8 8 0 0 1 0-4zm4.9 0h5.6a17 17 0 0 1 0 4H9.2a17 17 0 0 1 0-4zm7.5 0h3a8 8 0 0 1 0 4h-3a19 19 0 0 0 0-4zM9.2 15h5.6c-.6 3.3-1.9 5-2.8 5s-2.2-1.7-2.8-5z"/></svg>www.gentlepathcare.com</li>
  </ul>

  <ul class="phones">
    <li>201.555.0148 <svg viewBox="0 0 24 24"><path d="M6.6 10.8a15 15 0 0 0 6.6 6.6l2.2-2.2c.3-.3.7-.4 1-.2 1.1.4 2.3.6 3.6.6.6 0 1 .4 1 1V20c0 .6-.4 1-1 1A17 17 0 0 1 3 4c0-.6.4-1 1-1h3.5c.6 0 1 .4 1 1 0 1.3.2 2.5.6 3.6.1.3 0 .7-.2 1z"/></svg></li>
    <li>201.555.0163 <svg viewBox="0 0 24 24"><path d="M6 2h12v6H6zM4 9h16a2 2 0 0 1 2 2v6h-4v5H6v-5H2v-6a2 2 0 0 1 2-2zm4 8v3h8v-3z"/></svg></li>
  </ul>

  <div class="rule bottom"></div>

  <address class="address" style="font-style:normal">
    18 Birchwood Court, Suite 304<br>Holloway, NJ 07519
  </address>
</section>

</body>
</html>
```